Postcard design for Valdane Roofing

Looking to get a professional postcard for my roofing company. Card must include VR company logo, KT certified logo (in upload files) and also the following writing: Need a new roof? Dont wait call us today for your free estimate (613) 555-3916 (Adress: 4172 Township road 42, Harwick ON K0C2M0 In Bullet I would like the following: Fully Insured, Residential, Commercial, Re-roofing, Repairs, KT certified installer.. I would like to have in bold: Financing available. www.valdaneroofing-example.com.

I would like half or 3/4 of the background to be a nice house with a clear view of the shingle roof just like the one (or use that one if quality is good enough) in my uploaded files.

Would love to keep a theme similar to my buisness card

• double sided

```html
<!DOCTYPE html>
<html lang="en">
<head>
<meta charset="utf-8">
<title>Valdane Roofing Postcard</title>
<link href="https://fonts.googleapis.com/css2?family=Roboto:ital,wght@0,400;0,500;0,700;0,900;1,400&family=Roboto+Condensed:wght@700&display=swap" rel="stylesheet">
<style>
  :root{
    --board:#2a456e;
    --navy:#1d4583;
    --navy-deep:#17396f;
    --white:#ffffff;
    --ink:#2b2b2b;
    --badge:#c8242b;
    --sky:#6ea3d6;
    --roof:#8b8a84;
    --brick:#c9ad7a;
    --lawn:#5f8d3a;
    --gravel:#8a7f72;
    --shadow:#d8d6d6;
  }
  *{box-sizing:border-box;margin:0;padding:0}
  html,body{width:1200px;height:1200px;overflow:hidden;background:var(--board)}
  body{position:relative;font-family:"Roboto",Arial,sans-serif}
  .nowrap{white-space:nowrap}
  .card{position:absolute;background:var(--white)}
  .photo-house{position:absolute;background:linear-gradient(180deg,var(--sky) 0%,#a9c3da 22%,var(--roof) 40%,#7d7a72 58%,var(--brick) 72%,var(--lawn) 86%,var(--gravel) 100%)}
  .photo-shingles{position:absolute;background:radial-gradient(circle at 40% 10%,#d7b04a 0%,transparent 10%),linear-gradient(160deg,#4a3a33 0%,#7b6b61 45%,#968b80 100%)}
  .brand{color:var(--navy);font-weight:900;text-align:center;line-height:1;letter-spacing:.04em;display:flex;flex-direction:column;align-items:center}
  .brand-mark{width:22px;height:22px;border:3px solid currentColor;margin-bottom:8px}
  .brand-name{font-size:21px}
  .brand-sub{font-size:9px;letter-spacing:.9em;margin-top:4px;font-weight:900}
  .badge{position:absolute;border-radius:50%;background:var(--badge);box-shadow:inset 0 0 0 5px #e8e2dc}
  .board-label{position:absolute;font-family:"Roboto Condensed","Roboto",sans-serif;font-weight:700;color:var(--white);font-size:58px;letter-spacing:.01em;line-height:1}

  /* Design 1 */
  .design-one{left:21px;top:45px;width:562px;height:436px}
  .design-one .photo-house{left:0;top:0;width:324px;height:436px}
  .design-one .estimate{position:absolute;left:15px;top:360px;width:311px;background:var(--navy);color:var(--white);font-size:14.5px;line-height:23px;padding:4px 7px}
  .design-one .estimate b{font-weight:500}
  .design-one .panel{position:absolute;left:324px;top:0;width:238px;height:436px;text-align:center}
  .design-one .brand{position:absolute;left:0;right:0;top:52px}
  .design-one .financing{position:absolute;left:0;right:0;top:142px;color:var(--navy);font-weight:700;font-size:16px;white-space:nowrap}
  .design-one .url{position:absolute;left:0;right:0;top:164px;color:var(--navy);font-weight:700;font-size:13px;white-space:nowrap}
  .design-one .services{position:absolute;left:0;right:0;top:197px;list-style:none;font-style:italic;font-size:14px;line-height:20.5px;color:var(--ink)}
  .design-one .badge{left:401px;top:337px;width:68px;height:68px}

  /* Design 2 */
  .design-two{left:614px;top:222px;width:562px;height:436px}
  .design-two .photo-house{left:14px;top:16px;width:534px;height:313px}
  .design-two .services-tab{position:absolute;left:14px;top:178px;width:96px;height:151px}
  .design-two .services{position:absolute;left:21px;top:212px;list-style:none;color:var(--white);font-size:11.5px;line-height:16.5px;font-weight:500;white-space:nowrap}
  .design-two .services li::before{content:"";display:inline-block;width:5px;height:5px;border-radius:50%;background:var(--white);margin-right:5px;vertical-align:middle}
  .design-two .services .wrap{padding-left:10px}
  .design-two .services .wrap::before{display:none}
  .design-two .tag{position:absolute;background:var(--navy);color:var(--white);font-weight:700;text-align:center;line-height:26px;white-space:nowrap}
  .design-two .tag-financing{left:330px;top:262px;width:204px;height:26px;font-size:16px;letter-spacing:.02em}
  .design-two .tag-url{left:284px;top:296px;width:250px;height:26px;font-size:14px}
  .design-two .estimate{position:absolute;left:18px;top:350px;width:270px;font-size:15px;line-height:23px;color:var(--ink);letter-spacing:.01em}
  .design-two .estimate b{color:var(--navy);font-weight:500}
  .design-two .brand{position:absolute;left:310px;top:344px;width:140px}
  .design-two .badge{left:474px;top:343px;width:70px;height:70px}

  /* Back */
  .design-back{left:244px;top:704px;width:610px;height:472px}
  .design-back .shadow{position:absolute;left:8px;top:10px;width:292px;height:390px;background:var(--shadow)}
  .design-back .photo-shingles{left:0;top:0;width:292px;height:346px}
  .design-back .brand{position:absolute;left:120px;top:78px;width:150px;color:var(--white)}
  .design-back .services{position:absolute;left:91px;top:160px;width:209px;height:154px;background:var(--navy);list-style:none;color:var(--white);font-style:italic;font-size:18px;line-height:22.2px;text-align:center;padding-top:10px;white-space:nowrap}
  .design-back .financing{position:absolute;left:0;top:346px;width:292px;height:44px;background:var(--navy-deep);color:var(--white);font-weight:700;font-size:22px;line-height:44px;text-align:center;letter-spacing:.02em;white-space:nowrap}
  .design-back .stamp{position:absolute;left:465px;top:24px;width:122px;height:126px;border:1px solid #555}
  .design-back .address-line{position:absolute;left:305px;width:280px;border-top:1px solid #444}
</style>
</head>
<body>

  <div class="board-label" style="left:158px;top:512px">DESIGN1</div>
  <div class="board-label" style="left:760px;top:152px">DESIGN2</div>
  <div class="board-label" style="left:903px;top:868px;text-align:center;line-height:1.6">BACK<br>DESIGN</div>

  <section class="card design-one">
    <div class="photo-house" role="img" aria-label="Photo of a large brick house with a grey shingle roof and arched windows"></div>
    <p class="estimate">Need a new roof? Dont wait call us today for your free estimate&nbsp; <b class="nowrap">(613) 555-3916</b></p>
    <div class="panel">
      <div class="brand"><span class="brand-mark"></span><span class="brand-name">VALDANE</span><span class="brand-sub">ROOFING</span></div>
      <p class="financing">FINANCING AVAILABLE</p>
      <p class="url">www.valdaneroofing-example.com</p>
      <ul class="services">
        <li>Fully Insured</li><li>Residential</li><li>Commercial</li><li>Re-roofing</li><li>Repairs</li><li>KT certified installer</li>
      </ul>
    </div>
    <div class="badge" role="img" aria-label="Certified roofer badge"></div>
  </section>

  <section class="card design-two">
    <div class="photo-house" role="img" aria-label="Photo of a brick house with a wide grey shingle roof, garage and evergreen trees"></div>
    <svg class="services-tab" viewBox="0 0 96 151" aria-hidden="true"><polygon points="0,28 48,0 96,28 96,151 0,151" fill="var(--navy)"/></svg>
    <ul class="services">
      <li>Fully Insured</li><li>Residential</li><li>Commercial</li><li>Re-roofing</li><li>Repairs</li><li>KT Certified</li><li class="wrap">Installer</li>
    </ul>
    <div class="tag tag-financing">FINANCING AVAILABLE</div>
    <div class="tag tag-url">www.valdaneroofing-example.com</div>
    <p class="estimate">Need a new roof? Dont wait call us today for your free estimate<br><b>(613) 555-3916</b></p>
    <div class="brand"><span class="brand-mark"></span><span class="brand-name">VALDANE</span><span class="brand-sub">ROOFING</span></div>
    <div class="badge" role="img" aria-label="Certified roofer badge"></div>
  </section>

  <section class="card design-back">
    <div class="shadow"></div>
    <div class="photo-shingles" role="img" aria-label="Close-up photo of asphalt roof shingles with a yellow leaf"></div>
    <div class="brand"><span class="brand-mark"></span><span class="brand-name">VALDANE</span><span class="brand-sub">ROOFING</span></div>
    <ul class="services">
      <li>Fully Insured</li><li>Residential</li><li>Commercial</li><li>Re-roofing</li><li>Repairs</li><li>KT certified installer</li>
    </ul>
    <div class="financing">FINANCING AVAILABLE</div>
    <div class="stamp"></div>
    <div class="address-line" style="top:234px"></div>
    <div class="address-line" style="top:256px"></div>
    <div class="address-line" style="top:278px"></div>
    <div class="address-line" style="top:300px"></div>
    <div class="address-line" style="top:322px"></div>
    <div class="address-line" style="top:344px"></div>
  </section>

</body>
</html>
```